Verdant Loop Advisors, LLC

I am looking for a simple, clear layout with my logo prominent and embossed, on the best quality card stock available. I would like the business name and phone number included on the card as well......I dont want my name anywhere on the card and I would like my logo embossed on the card......something simple with a white back......open to designs as long as they go along with recycling symbols and green type stuff.....The address, website, cell number, fax number, and email are listed below

5374 Tillbury Fenwood Road
Carrow Heights, MD 20899

c. 240.555.0143 f. 240.555.0187
e. sales@verdantloopadvisors.example
w. www.verdantloopadvisors.example

Industry/Entity Type

Recycling

```html
<!DOCTYPE html>
<html lang="en">
<head>
<meta charset="utf-8">
<title>Verdant Loop Advisors, LLC — Business Card</title>
<link rel="stylesheet" href="https://fonts.googleapis.com/css2?family=Arimo:wght@400;700&display=swap">
<style>
  :root {
    --backdrop: #e9e9e9;
    --card-stock: #f8f7f2;
    --brand-green: #2b6a2a;
    --ink: #2e2e2e;
    --icon: #3a3a3a;
  }
  * { box-sizing: border-box; margin: 0; padding: 0; }
  html, body {
    width: 1200px; height: 1200px; overflow: hidden;
    background: var(--backdrop);
    font-family: "Arimo", Arial, sans-serif;
  }
  .card {
    position: absolute;
    left: 60px; top: 290px;
    width: 1080px; height: 620px;
    background: var(--card-stock);
    overflow: hidden;
    box-shadow: 0 2px 6px rgba(0,0,0,0.12);
  }
  .brand-mark-area {
    position: absolute;
    left: -300px; top: -10px;
    width: 640px; height: 640px;
    border-radius: 50%;
    background: var(--brand-green);
  }
  .wordmark {
    position: absolute;
    right: 64px; top: 82px;
    display: flex; align-items: center; gap: 14px;
    color: var(--brand-green);
    font-weight: 700;
    text-transform: uppercase;
  }
  .wordmark-dot {
    width: 40px; height: 40px;
    background: var(--brand-green);
    border-radius: 50%;
  }
  .wordmark-name {
    font-size: 38px; line-height: 1; letter-spacing: 2px;
  }
  .wordmark-name small {
    display: block;
    font-size: 15px; letter-spacing: 8.6px; margin-top: 5px;
  }
  .contact {
    position: absolute;
    right: 44px; top: 380px;
    list-style: none;
    color: var(--ink);
    font-size: 19px;
    text-align: right;
  }
  .contact li {
    display: flex; justify-content: flex-end; align-items: center;
    gap: 10px; margin-bottom: 17px;
  }
  .contact li.address { align-items: flex-start; line-height: 1.5; }
  .contact .icon { width: 20px; height: 20px; flex: none; fill: var(--icon); }
  .contact .phone-pair { display: flex; align-items: center; gap: 8px; }
</style>
</head>
<body>
  <div class="card">
    <div class="brand-mark-area" role="img" aria-label="Large green recycling mark decoration"></div>

    <div class="wordmark">
      <span class="wordmark-dot"></span>
      <span class="wordmark-name">Verdant Loop<small>Advisors, LLC</small></span>
    </div>

    <ul class="contact">
      <li class="address">
        <span>5374 Tillbury Fenwood Road<br>Carrow Heights, MD 20899</span>
        <svg class="icon" viewBox="0 0 20 20" aria-hidden="true"><path d="M10 1a6 6 0 0 0-6 6c0 4.5 6 12 6 12s6-7.5 6-12a6 6 0 0 0-6-6zm0 8.5A2.5 2.5 0 1 1 10 4.5a2.5 2.5 0 0 1 0 5z"/></svg>
      </li>
      <li>
        <span class="phone-pair">240.555.0143
          <svg class="icon" viewBox="0 0 20 20" aria-hidden="true"><rect x="6" y="2" width="8" height="16" rx="1.5"/><rect x="7.5" y="4" width="5" height="8" fill="#f8f7f2"/></svg>
        </span>
        <span class="phone-pair">240.555.0187
          <svg class="icon" viewBox="0 0 20 20" aria-hidden="true"><path d="M2 7c0-2 3.5-3.5 8-3.5S18 5 18 7v1.5h-4V6.8c-1-.5-2.5-.7-4-.7s-3 .2-4 .7v1.7H2z"/><path d="M5 10h10l2 6H3z"/></svg>
        </span>
      </li>
      <li>
        <span>sales@verdantloopadvisors.example</span>
        <svg class="icon" viewBox="0 0 20 20" aria-hidden="true"><text x="10" y="15.5" text-anchor="middle" font-size="17" font-family="Arimo, Arial, sans-serif" font-weight="700">@</text></svg>
      </li>
      <li>
        <span>www.verdantloopadvisors.example</span>
        <svg class="icon" viewBox="0 0 20 20" aria-hidden="true"><rect x="5" y="5" width="9" height="13" rx="4.5"/><path d="M9.5 5V2.5h6" fill="none" stroke="#3a3a3a" stroke-width="1.4"/></svg>
      </li>
    </ul>
  </div>
</body>
</html>
```